Kem7Dex Letterhead

Need a new letterhead for my law firm.
IDENTIFYING INFORMATION BELOW:
Ansel T Brightwater III
Attorney at Law
Address: 4832 Tillbury Rd, Ste 250, Dallas, TX 75204
Phone: 866-402-7183
Fax: 469-583-0271
Email: kem@kem7dex.example
Website: www.kem7dex.example

Colors
0054AA
0677BA
7BADD7
CADEEF
E8F1F8

Requirements
Must have
• Logo needs to be on the letterhead, along with identifying information which is included in the project description.

```html
<!DOCTYPE html>
<html lang="en">
<head>
<meta charset="utf-8">
<title>Kem7Dex Letterhead</title>
<link href="https://fonts.googleapis.com/css2?family=Montserrat:wght@400;500;700&display=swap" rel="stylesheet">
<style>
  :root {
    --blue-deep: #0054AA;
    --blue: #0677BA;
    --blue-mid: #7BADD7;
    --blue-light: #CADEEF;
    --blue-pale: #E8F1F8;
    --ink: #1a1a1a;
    --grey: #6b6b6b;
    --rule: #c9c9c9;
    --paper: #ffffff;
  }
  * { margin: 0; padding: 0; box-sizing: border-box; }
  html, body { width: 800px; height: 1200px; overflow: hidden; background: var(--paper); }
  body { font-family: "Montserrat", Arial, sans-serif; color: var(--ink); }
  .letterhead { position: relative; width: 800px; height: 1200px; background: var(--paper); }
  .edge { position: absolute; left: 0; width: 800px; height: 34px; }
  .edge--top { top: 0; }
  .edge--bottom { bottom: 0; transform: scaleY(-1); }

  .brand { position: absolute; left: 76px; top: 120px; }
  .brand__name {
    font-weight: 500; font-size: 38px; letter-spacing: 0;
    color: var(--ink); line-height: 1;
  }
  .brand__tagline {
    margin-top: 10px; font-size: 13px; font-weight: 500;
    letter-spacing: 3.4px; color: var(--grey);
  }

  .sender { position: absolute; right: 76px; top: 112px; text-align: right; font-style: normal; }
  .sender__name { font-size: 17px; font-weight: 700; color: var(--blue); letter-spacing: .3px; }
  .sender__title { margin-top: 3px; font-size: 12px; color: var(--grey); }
  .sender__address { margin-top: 14px; font-size: 11.5px; line-height: 1.55; color: var(--ink); }

  .contact-bar {
    position: absolute; left: 60px; right: 60px; top: 1060px;
    display: flex;
  }
  .contact {
    flex: 1; display: flex; flex-direction: column; align-items: center;
    border-left: 1px solid var(--rule);
  }
  .contact:first-child { border-left: none; }
  .contact__icon { width: 30px; height: 30px; }
  .contact__text { margin-top: 12px; font-size: 11.5px; color: var(--ink); white-space: nowrap; }
</style>
</head>
<body>
<div class="letterhead">
  <svg class="edge edge--top" viewBox="0 0 800 34" aria-hidden="true">
    <defs>
      <linearGradient id="tabL" x1="0" x2="1">
        <stop offset="0" stop-color="#0054AA"/><stop offset="1" stop-color="#0677BA"/>
      </linearGradient>
      <linearGradient id="tabR" x1="1" x2="0">
        <stop offset="0" stop-color="#0054AA"/><stop offset="1" stop-color="#0677BA"/>
      </linearGradient>
    </defs>
    <rect x="0" y="0" width="800" height="8" fill="#111"/>
    <polygon points="0,0 118,0 96,22 0,22" fill="url(#tabL)"/>
    <polygon points="96,22 118,0 124,0 100,26 0,26 0,22" fill="#7BADD7"/>
    <polygon points="800,0 682,0 704,22 800,22" fill="url(#tabR)"/>
    <polygon points="704,22 682,0 676,0 700,26 800,26 800,22" fill="#7BADD7"/>
  </svg>

  <header class="brand">
    <div class="brand__name">Kem7Dex</div>
    <div class="brand__tagline">STEADY COUNSEL</div>
  </header>

  <address class="sender">
    <div class="sender__name">ANSEL T BRIGHTWATER III</div>
    <div class="sender__title">Attorney at Law</div>
    <div class="sender__address">4832 Tillbury Rd, Ste 250<br>Dallas, TX 75204</div>
  </address>

  <footer class="contact-bar">
    <div class="contact">
      <svg class="contact__icon" viewBox="0 0 30 30" aria-label="Phone">
        <circle cx="15" cy="15" r="15" fill="var(--blue)"/>
        <path d="M11 8.5l2.3 0 1 3.2-1.5 1.2c.8 1.7 2 2.9 3.7 3.7l1.2-1.5 3.2 1v2.3c0 .8-.7 1.4-1.5 1.3C14 19 10.9 15.9 9.8 10c-.1-.8.4-1.5 1.2-1.5z" fill="#fff"/>
      </svg>
      <div class="contact__text">866-402-7183</div>
    </div>
    <div class="contact">
      <svg class="contact__icon" viewBox="0 0 30 30" aria-label="Fax">
        <circle cx="15" cy="15" r="15" fill="var(--blue)"/>
        <rect x="11" y="8" width="8" height="5" fill="#fff"/>
        <rect x="8.5" y="12.5" width="13" height="7" rx="1" fill="#fff"/>
        <rect x="11" y="17" width="8" height="5" fill="#fff" stroke="var(--blue)" stroke-width="1"/>
      </svg>
      <div class="contact__text">469-583-0271</div>
    </div>
    <div class="contact">
      <svg class="contact__icon" viewBox="0 0 30 30" aria-label="Email">
        <circle cx="15" cy="15" r="15" fill="var(--blue)"/>
        <rect x="8" y="10" width="14" height="10" rx="1" fill="#fff"/>
        <path d="M8.5 10.5l6.5 5 6.5-5" fill="none" stroke="var(--blue)" stroke-width="1.2"/>
      </svg>
      <div class="contact__text">kem@kem7dex.example</div>
    </div>
    <div class="contact">
      <svg class="contact__icon" viewBox="0 0 30 30" aria-label="Website">
        <circle cx="15" cy="15" r="15" fill="var(--blue)"/>
        <g fill="none" stroke="#fff" stroke-width="1.3">
          <circle cx="15" cy="15" r="6.5"/>
          <ellipse cx="15" cy="15" rx="2.8" ry="6.5"/>
          <path d="M8.5 15h13"/>
        </g>
      </svg>
      <div class="contact__text">www.kem7dex.example</div>
    </div>
  </footer>

  <svg class="edge edge--bottom" viewBox="0 0 800 34" aria-hidden="true">
    <rect x="0" y="0" width="800" height="8" fill="#111"/>
    <polygon points="0,0 118,0 96,22 0,22" fill="url(#tabL)"/>
    <polygon points="96,22 118,0 124,0 100,26 0,26 0,22" fill="#7BADD7"/>
    <polygon points="800,0 682,0 704,22 800,22" fill="url(#tabR)"/>
    <polygon points="704,22 682,0 676,0 700,26 800,26 800,22" fill="#7BADD7"/>
  </svg>
</div>
</body>
</html>
```